Association qui souhaite améliorer l'accès aux personnes en situation de handicap

Nous sommes une association qui a pour objectif d'améliorer l'accessibilité, augmenter l'offre des activités réalisables dans notre région touristique.
Nous souhaitons réaliser un site internet afin de pouvoir communiquer sur notre association. Nous avons déjà conçu notre flyer sur Graphivolte. Nous souhaiterions une base graphique se rapportant à celui-ci. C'est possible de tout retravailler mais nous souhaitons tout de même retrouver la charte graphique ou code couleur du flyer.
Il nous faudrait quelques pages:
- 1 page : Acceuil / Présentation (Home), Il y aurait le descriptif de l'association, avec ses objectifs à +/- moyen terme
- 1 page : Nos réalisations, celle-ci présenterait les éléments que nous avons réalisés avec des zones de textes et des images classées chronologiquement au fur et à mesure des nouveautés
- 1 page : Media, comme la précédente, mais ou on pourrait voir ou lire sur les divers médias qui parlent de nous
- 1 page : Evenements : c'est une page pour présenter divers activités que nous allons organiser
- 1 page : Contact qui indique comment nous contacter et avec la présentation des 5 ou 6 membres du comité
- 1 link donate : qui arrive sur un formulaire de donnée que l'on pourra faire évoluer sur un système de payement par la suite. Cette bannière doit se retrouver sur toutes les pages
Il est nécessaire que se design puisse être transféré sur une lecture sur téléphone mobile
Personnes en situation de handicap
Associatif
Coded - Design and coding required
5+ page

```html
<!DOCTYPE html>
<html lang="en">
<head>
<meta charset="utf-8">
<title>OpenPath Association</title>
<link href="https://fonts.googleapis.com/css2?family=Bebas+Neue&family=Montserrat:wght@400;500;600;700&display=swap" rel="stylesheet">
<style>
:root{
  --red:#c1181f;
  --ink:#2e3a3d;
  --footer:#333d40;
  --muted:#8a9396;
  --field:#f2f2f2;
  --white:#fff;
}
*{box-sizing:border-box;margin:0;padding:0}
html,body{width:1200px;height:4800px;overflow:hidden}
body{position:relative;background:var(--white);font-family:'Montserrat',sans-serif;color:var(--ink)}
.abs{position:absolute}
.display{font-family:'Bebas Neue',sans-serif;font-weight:400;color:var(--ink);line-height:.95}
.brand{display:flex;align-items:center;gap:10px;font-family:'Montserrat',sans-serif;font-weight:700;color:var(--ink);font-size:20px;line-height:1;white-space:nowrap}
.brand .mark{width:22px;height:22px;background:var(--red);flex:none}
.nav{left:407px;top:44px;display:flex;gap:30px;font-size:12px;font-weight:600;letter-spacing:1.5px}
.nav .active{color:var(--red)}
.btn{background:var(--red);color:var(--white);font-weight:600;display:flex;align-items:center;justify-content:center}
.donate{left:993px;top:32px;width:130px;height:42px;font-size:15px}
.photo{background:linear-gradient(135deg,#8a5a3c,#c9a07c 45%,#5b3b48);}
.hero-photo{left:609px;top:115px;width:591px;height:485px}
.hero-title{left:75px;top:228px;font-size:100px;line-height:.75;white-space:nowrap}
.learn{left:75px;top:499px;width:141px;height:47px;font-size:14px}
.underline{position:relative;display:inline-block}
.underline::after{content:"";position:absolute;left:4%;right:2%;bottom:-6px;height:3px;background:var(--red);border-radius:50%/3px;transform:rotate(-1deg)}
.intro-title{left:0;width:1200px;top:717px;text-align:center;font-size:66px}
.intro-text{left:160px;width:880px;top:894px;text-align:center;font-size:17.5px;line-height:1.3}
.audience{width:338px;height:133px;border:2px solid var(--red);border-radius:4px;display:flex;align-items:center;padding:0 26px 0 24px;justify-content:space-between;gap:12px}
.audience .icon{width:34px;height:80px;background:var(--red);border-radius:17px 17px 6px 6px;flex:none}
.audience .label{font-family:'Bebas Neue',sans-serif;font-size:44px;color:var(--ink);white-space:nowrap}
.programs-band{left:0;top:1490px;width:1200px;height:770px}
.programs-title{left:75px;top:1723px;font-size:66px;color:var(--white)}
.card{width:337px;background:var(--white)}
.card .photo{height:216px}
.card h3{font-family:'Bebas Neue',sans-serif;font-weight:400;font-size:40px;color:var(--ink);margin:12px 0 0 18px;line-height:1}
.card p{font-size:19px;line-height:1.2;margin:4px 40px 0 18px;color:var(--ink)}
.p1{background:linear-gradient(160deg,#9aa0a4,#5c6166)}
.p2{background:linear-gradient(160deg,#9b5a4a,#5a2630)}
.p3{background:linear-gradient(160deg,#5e5040,#2e6b8c)}
.mission-title{left:0;width:1200px;top:2347px;text-align:center;font-size:68px}
.mission-text{left:120px;width:960px;top:2455px;text-align:center;font-size:18.5px;line-height:1.22}
.join-photo{left:0;top:2664px;width:1200px;height:466px;background:linear-gradient(120deg,#3f4a3e,#5a6452 50%,#3c443c)}
.join-logo{left:738px;top:2830px;width:387px;height:130px;background:var(--white);display:flex;align-items:center;justify-content:center}
.join-logo .brand{font-size:27px}
.join-cta{left:574px;top:2960px;width:551px;height:123px;background:var(--red);display:flex;align-items:center;justify-content:center}
.join-cta span{font-family:'Bebas Neue',sans-serif;font-size:72px;color:var(--white)}
.partners{left:0;top:3130px;width:1200px;height:141px;background:var(--red);display:flex;align-items:center;justify-content:space-between;padding:0 62px}
.partners span{font-weight:700;color:var(--white);font-size:22px}
.news-title{left:75px;top:3325px;font-size:68px}
.lm-title{left:102px;top:3977px;font-size:48px;line-height:.98}
.lm-text{left:102px;top:4089px;width:520px;font-size:16px;line-height:1.55}
.form{left:699px;top:3946px;width:424px;height:389px;border:2px solid var(--ink);border-radius:6px}
.field{position:absolute;left:27px;width:369px;height:44px;background:var(--field);font-size:14px;font-weight:500;display:flex;align-items:center;padding-left:14px}
.submit{position:absolute;left:27px;top:314px;width:111px;height:45px;font-size:15px}
.footer{left:0;top:4430px;width:1200px;height:370px;background:var(--footer);color:var(--muted);font-size:12.5px}
.footer .logo-box{position:absolute;left:75px;top:69px;width:197px;height:65px;background:var(--white);display:flex;align-items:center;justify-content:center}
.footer .logo-box .brand{font-size:13px;gap:7px}
.footer h4{color:var(--white);font-size:13px;font-weight:600;margin-bottom:14px}
.footer .col{position:absolute;top:65px;line-height:1.25}
.footer .col li{list-style:none;margin-bottom:14px}
.footer .addr{position:absolute;left:75px;top:162px;line-height:2.2}
.footer .rule{position:absolute;left:75px;right:75px;top:283px;height:1px;background:#4a5457}
.footer .copy{position:absolute;left:75px;top:302px;font-size:11px}
</style>
</head>
<body>

<header>
  <div class="abs brand" style="left:75px;top:45px;font-size:22px"><span class="mark"></span>OpenPath Association</div>
  <nav class="abs nav">
    <span class="active">HOME</span><span>WHY CHOOSE US</span><span>BENEFITS</span><span>TESTIMONIALS</span><span>CONTACT</span>
  </nav>
  <div class="abs btn donate">Donate Now</div>
</header>

<section class="hero">
  <div class="abs photo hero-photo" role="img" aria-label="Photo of friends toasting, one in a wheelchair"></div>
  <svg class="abs" style="left:609px;top:415px" width="591" height="190" viewBox="0 0 591 190">
    <polygon points="0,185 591,0 591,190 0,190" fill="#fff"/>
    <polygon points="0,175 591,25 591,80 40,180" fill="#c1181f"/>
  </svg>
  <h1 class="abs display hero-title">Advancing the rights<br>of persons with<br>disabilities</h1>
  <div class="abs btn learn">Learn More</div>
</section>

<section class="intro">
  <h2 class="abs display intro-title">Advancing the rights<br>of persons with <span class="underline">disabilities</span></h2>
  <p class="abs intro-text">Lorem ipsum dolor sit amet, consectetur adipiscing elit, sed do eiusmod tempor incididunt ut labore et dolore magna aliqua. Ut enim ad minim veniam, quis nostrud exercitation ullamco laboris nisi ut aliquip ex ea commodo consequat. Duis aute irure dolor in reprehenderit in voluptate velit esse cillum dolore eu fugiat nulla pariatur. Excepteur sint occaecat cupidatat non proident, sunt in culpa qui officia deserunt mollit anim id est laborum.</p>
  <div class="abs audience" style="left:75px;top:1110px"><span class="icon" role="img" aria-label="Parents icon"></span><span class="label">Parents</span></div>
  <div class="abs audience" style="left:430px;top:1110px"><span class="icon" role="img" aria-label="Educators icon"></span><span class="label">Educators</span></div>
  <div class="abs audience" style="left:788px;top:1110px"><span class="icon" role="img" aria-label="Adults icon"></span><span class="label">Adults</span></div>
  <div class="abs audience" style="left:75px;top:1263px"><span class="icon" role="img" aria-label="Professionals icon"></span><span class="label">Professionals</span></div>
  <div class="abs audience" style="left:430px;top:1263px"><span class="icon" role="img" aria-label="Students icon"></span><span class="label">Students</span></div>
</section>

<section class="programs">
  <svg class="abs programs-band" viewBox="0 0 1200 770" width="1200" height="770"><polygon points="0,0 1200,326 1200,770 0,770" fill="#c1181f"/></svg>
  <h2 class="abs display programs-title">Programs</h2>
  <article class="abs card" style="left:75px;top:1839px;height:361px"><div class="photo p1" role="img" aria-label="Photo of a smiling girl in a wheelchair"></div><h3>Lorem Ipsum</h3><p>Dolor sit amet, consectetur adipiscing elit, sed do eiusmod</p></article>
  <article class="abs card" style="left:431px;top:1839px;height:361px"><div class="photo p2" role="img" aria-label="Photo of two men laughing together"></div><h3>Lorem Ipsum</h3><p>Dolor sit amet, consectetur adipiscing elit, sed do eiusmod</p></article>
  <article class="abs card" style="left:788px;top:1839px;height:361px"><div class="photo p3" role="img" aria-label="Photo of friends chatting at a bar"></div><h3>Lorem Ipsum</h3><p>Dolor sit amet, consectetur adipiscing elit, sed do eiusmod</p></article>
</section>

<section class="mission">
  <h2 class="abs display mission-title"><span class="underline">Mission</span></h2>
  <p class="abs mission-text">Lorem ipsum dolor sit amet, consectetur adipiscing elit, sed do eiusmod tempor incididunt ut labore et dolore magna aliqua. Ut enim ad minim veniam, quis nostrud exercitation ullamco laboris nisi ut aliquip ex ea commodo consequat. Duis aute irure dolor in reprehenderit in voluptate velit esse cillum dolore eu fugiat nulla pariatur. Excepteur sint occaecat cupidatat non proident, sunt in culpa qui officia deserunt mollit anim id est laborum.</p>
</section>

<section class="join">
  <div class="abs join-photo" role="img" aria-label="Photo of a mother and son embracing, darkened"></div>
  <div class="abs join-logo"><div class="brand"><span class="mark"></span>OpenPath Association</div></div>
  <div class="abs join-cta"><span>Join the Association</span></div>
  <div class="abs partners"><span>Brightsmile</span><span>Linkwave</span><span>Hartwell</span><span>Northbank</span><span>Bean Harbor</span><span>Fizzco</span></div>
</section>

<section class="news">
  <h2 class="abs display news-title"><span class="underline">Latest</span> News</h2>
  <article class="abs card" style="left:75px;top:3443px"><div class="photo p1" role="img" aria-label="Photo of a smiling girl in a wheelchair"></div><h3>Lorem Ipsum</h3><p>Dolor sit amet, consectetur adipiscing elit, sed do eiusmod</p></article>
  <article class="abs card" style="left:431px;top:3443px"><div class="photo p2" role="img" aria-label="Photo of two men laughing together"></div><h3>Lorem Ipsum</h3><p>Dolor sit amet, consectetur adipiscing elit, sed do eiusmod</p></article>
  <article class="abs card" style="left:788px;top:3443px"><div class="photo p3" role="img" aria-label="Photo of friends chatting at a bar"></div><h3>Lorem Ipsum</h3><p>Dolor sit amet, consectetur adipiscing elit, sed do eiusmod</p></article>
</section>

<section class="learn-more">
  <h2 class="abs display lm-title"><span class="underline">Learn more</span> about our<br>programs</h2>
  <p class="abs lm-text">Lorem ipsum dolor sit amet, consectetur adipiscing elit, sed do eiusmod tempor incididunt ut labore et dolore magna aliqua. Ut enim ad minim veniam, quis nostrud exercitation ullamco laboris nisi ut aliquip ex ea commodo consequat. Duis aute irure dolor in reprehenderit in voluptate velit esse cillum dolore eu fugiat nulla pariatur. Excepteur sint occaecat cupidatat non proident, sunt in culpa qui officia deserunt mollit anim id est laborum.</p>
  <form class="abs form">
    <div class="field" style="top:26px">First Name</div>
    <div class="field" style="top:91px">Last Name</div>
    <div class="field" style="top:156px">Email</div>
    <div class="field" style="top:221px">Company Name</div>
    <div class="btn submit">Submit</div>
  </form>
</section>

<footer class="abs footer">
  <div class="logo-box"><div class="brand"><span class="mark" style="width:14px;height:14px"></span>OpenPath Association</div></div>
  <div class="addr"><h4 style="margin:0">Address</h4>OpenPath Association, 412 Meadow Lane,<br>Suite 8 Fairview, TX 75000</div>
  <div class="col" style="left:483px;width:230px"><h4>Core Principles</h4><ul><li>What are Learning Disabilities?</li><li>Evaluation and Identification of Learning Disabilities</li><li>Best Practices in the Use of Cognitive Assessment in Learning Disability Identification</li></ul></div>
  <div class="col" style="left:777px"><h4>Navigation</h4><ul><li>Home</li><li>About</li><li>Programs</li><li>Contact</li></ul></div>
  <div class="col" style="left:909px"><h4>Social</h4><ul><li>Picfeed</li><li>Townsquare</li></ul></div>
  <div class="col" style="left:1034px"><h4>Our Policies</h4><ul><li>Privacy Policy</li><li>Terms of Use</li></ul></div>
  <div class="rule"></div>
  <div class="copy">© 2022 OpenPath Association, All Rights Reserved</div>
</footer>

</body>
</html>
```